Improving the design of the attached webpage jpg image

Make the page professional, but keep it simple. All elements on the page can be changed to anything you like EXCEPT the blue bar at the top of the page.

The two images are the same page.

The content on the page must all be there. Do not add new content.

The design needs to feel like a professional score report.
Updates

Need extra days to review

Industry/Entity Type

Education

Number of Pages Required

1 page

Colors

Designer to choose colors to be used in the design.

Requirements
Must have
• The blue bar color and the bars themselves at the top and bottom of the page. All the content on the page.

```html
<!DOCTYPE html>
<html lang="en">
<head>
<meta charset="utf-8">
<title>Scorewise GradAdmit Score Report</title>
<link href="https://fonts.googleapis.com/css2?family=Montserrat:wght@400;500;600;700&display=swap" rel="stylesheet">
<style>
:root{
  --stage:#adb4bc;
  --brand-bar:#3d7690;
  --ink:#2f3a44;
  --ink-soft:#5b6670;
  --muted:#8f979e;
  --line:#e6e9ec;
  --head-bg:#f3f5f5;
  --track:#dedfe0;
  --red:#e8411e;
  --red-soft:#fde6e0;
  --orange:#ef8a1c;
  --green:#6cc551;
  --green-soft:#e9f7e4;
  --pill:#f2f3f4;
  --white:#ffffff;
}
*{box-sizing:border-box;margin:0;padding:0}
html,body{width:800px;height:1200px;overflow:hidden}
body{background:var(--stage);font-family:"Montserrat",Arial,sans-serif;color:var(--ink);position:relative}
.report{position:absolute;left:0;width:800px;height:520px;background:var(--white);overflow:hidden}
.report--sections{top:60px}
.report--questions{top:620px}
.brand-bar{height:31px;background:var(--brand-bar)}
.abs{position:absolute}
.report-title{left:82px;top:76px;font-size:13.5px;font-weight:600;color:var(--ink)}
.score-ring{left:85px;top:124px;width:54px;height:54px}
.score-ring__value{left:82px;top:140px;width:58px;text-align:center;font-size:16px;font-weight:600;color:var(--red)}
.score-ring__total{left:82px;top:184px;width:58px;text-align:center;font-size:7px;color:var(--ink-soft)}
.meta{left:157px;top:125px;display:flex;align-items:center;gap:12px;font-size:7px;font-weight:600;color:var(--ink)}
.meta__item{display:flex;align-items:center;gap:5px}
.summary{left:157px;top:144px;width:380px;font-size:6.6px;line-height:12.7px;color:var(--ink-soft)}
.tabs{left:82px;top:222px;width:636px;height:22px;border-bottom:1px solid var(--line)}
.tab{position:absolute;top:0;font-size:8.3px;color:var(--muted);white-space:nowrap;padding-bottom:6px}
.tab--active{color:var(--ink);font-weight:600;border-bottom:2px solid var(--brand-bar);height:22px}
.section-heading{left:82px;top:275px;font-size:12.5px;font-weight:600}
.score-table{left:82px;top:304px;width:636px;height:198px;border:1px solid var(--line)}
.score-table__head{height:28px;background:var(--head-bg);font-size:8px;color:var(--muted);position:relative}
.score-table__head span{position:absolute;top:9px}
.score-row{position:absolute;left:0;width:100%;height:38px}
.score-row__name{position:absolute;left:16px;top:14px;font-size:8px;font-weight:500}
.percentile{position:absolute;left:206px;top:8px;height:18px;padding:0 10px;border-radius:9px;background:var(--pill);font-size:8px;line-height:18px;color:var(--ink)}
.meter{position:absolute;left:340px;top:0;width:278px;height:30px}
.meter__labels span{position:absolute;top:3px;font-size:6.5px;color:var(--muted);transform:translateX(-50%)}
.meter__labels span:first-child{transform:none}
.meter__labels span:last-child{transform:translateX(-100%)}
.meter__track{position:absolute;left:0;top:18px;width:100%;height:4px;border-radius:2px;background:var(--track)}
.meter__fill{position:absolute;left:0;top:0;height:4px;border-radius:2px}
.meter__knob{position:absolute;top:-6px;height:15px;padding:0 4px;min-width:22px;border-radius:8px;border:1.5px solid var(--white);font-size:6.5px;font-weight:600;color:var(--white);line-height:12px;text-align:center;transform:translateX(-50%)}
.is-red{background:var(--red)}
.is-orange{background:var(--orange)}
.is-green{background:var(--green)}
.qa-heading{left:82px;top:272px;font-size:9.5px;font-weight:600}
.filters{left:446px;top:266px;display:flex;gap:5px}
.filter{height:26px;padding:0 10px;border-radius:13px;border:1px solid var(--line);font-size:7.6px;line-height:24px;color:var(--ink-soft);background:var(--white)}
.filter--active{background:var(--brand-bar);border-color:var(--brand-bar);color:var(--white);font-weight:600}
.avg-time{left:84px;top:320px;display:flex;align-items:center;gap:7px;font-size:7.6px;font-weight:600;line-height:10px}
.time-pill{top:314px;width:72px;height:38px;border-radius:19px;border:1.5px solid var(--line);text-align:center;padding-top:7px}
.time-pill strong{display:block;font-size:8px;font-weight:600}
.time-pill small{display:block;font-size:7.4px;color:var(--muted);margin-top:1px}
.time-pill--expected{left:216px}
.time-pill--you{left:300px;border:2px solid var(--brand-bar)}
.question-table{left:82px;top:374px;width:636px;height:180px;border:1px solid var(--line)}
.question-table__head{height:27px;background:var(--head-bg);font-size:7.8px;color:var(--muted);position:relative}
.question-table__head span{position:absolute;top:9px}
.q-row{position:absolute;left:0;width:100%;height:35px;font-size:7.8px}
.q-row > *{position:absolute;top:9px}
.q-num{left:16px;top:14px}
.tag{height:17px;line-height:17px;padding:0 10px;border-radius:9px;font-size:7.6px;font-weight:500}
.tag--bad{background:var(--red-soft);color:var(--red)}
.tag--good{background:var(--green-soft);color:var(--green)}
.tag--type{background:var(--pill);color:var(--ink-soft);font-weight:400}
</style>
</head>
<body>

<section class="report report--sections">
  <div class="brand-bar"></div>
  <h1 class="abs report-title">Scorewise GradAdmit Score Report</h1>
  <svg class="abs score-ring" viewBox="0 0 54 54" aria-hidden="true">
    <circle cx="27" cy="27" r="25" fill="none" stroke="#e5e7e9" stroke-width="2.5"/>
    <circle cx="27" cy="27" r="25" fill="none" stroke="#e8411e" stroke-width="2.5" stroke-dasharray="19 158" transform="rotate(-90 27 27)" stroke-linecap="round"/>
  </svg>
  <div class="abs score-ring__value">275</div>
  <div class="abs score-ring__total">275/805</div>
  <div class="abs meta">
    <span class="meta__item"><svg width="9" height="9" viewBox="0 0 10 10" fill="none" stroke="#8f979e" stroke-width=".8"><rect x="1" y="1.8" width="8" height="7.4" rx="1"/><path d="M1 4h8M3 .8v2M7 .8v2"/></svg>September 4, 2024</span>
    <span class="meta__item"><svg width="8" height="9" viewBox="0 0 8 10" fill="none" stroke="#8f979e" stroke-width=".8"><path d="M1 .6h4l2 2v6.8H1z M2.5 5h3M2.5 7h3"/></svg>Simulation test 2</span>
  </div>
  <p class="abs summary">From classic novels like "Morning at Wrenfield" by Clara Whitcombe to contemporary bestsellers like "The Lantern Keeper" by M.R. Ashdown, literature transcends time and culture, touching the hearts and minds of readers. The power of storytelling allows us to escape reality, gain empathy, and explore diverse perspectives, making literature an indispensable part of the human experience.</p>
  <nav class="abs tabs">
    <span class="tab tab--active" style="left:0">Overall performance</span>
    <span class="tab" style="left:107px">Quantitative reasoning</span>
    <span class="tab" style="left:225px">Verbal reasoning</span>
    <span class="tab" style="left:317px">Data insights</span>
  </nav>
  <h2 class="abs section-heading">Section performance</h2>
  <div class="abs score-table">
    <div class="score-table__head"><span style="left:16px">Section</span><span style="left:206px">Percentile</span><span style="left:340px">Score</span></div>
    <div class="score-row" style="top:36px">
      <span class="score-row__name">Overall performance</span>
      <span class="percentile">1th</span>
      <div class="meter"><div class="meter__labels"><span style="left:0">205</span><span style="left:65%">546</span><span style="left:100%">805</span></div>
        <div class="meter__track"><div class="meter__fill is-red" style="width:31%"></div><span class="meter__knob is-red" style="left:31%">275</span></div></div>
    </div>
    <div class="score-row" style="top:74px">
      <span class="score-row__name">Quantitative reasoning</span>
      <span class="percentile">2th</span>
      <div class="meter"><div class="meter__labels"><span style="left:0">60</span><span style="left:64%">78</span><span style="left:100%">90</span></div>
        <div class="meter__track"><div class="meter__fill is-red" style="width:27%"></div><span class="meter__knob is-red" style="left:27%">63</span></div></div>
    </div>
    <div class="score-row" style="top:112px">
      <span class="score-row__name">Verbal reasoning</span>
      <span class="percentile">1th</span>
      <div class="meter"><div class="meter__labels"><span style="left:0">60</span><span style="left:61%">75</span><span style="left:100%">90</span></div>
        <div class="meter__track"><div class="meter__fill is-orange" style="width:52%"></div><span class="meter__knob is-orange" style="left:52%">65</span></div></div>
    </div>
    <div class="score-row" style="top:150px">
      <span class="score-row__name">Data insights</span>
      <span class="percentile">5th</span>
      <div class="meter"><div class="meter__labels"><span style="left:0">60</span><span style="left:56%">73</span><span style="left:100%">90</span></div>
        <div class="meter__track"><div class="meter__fill is-green" style="width:80%"></div><span class="meter__knob is-green" style="left:80%">80</span></div></div>
    </div>
  </div>
</section>

<section class="report report--questions">
  <div class="brand-bar"></div>
  <h1 class="abs report-title">Scorewise GradAdmit Score Report</h1>
  <svg class="abs score-ring" viewBox="0 0 54 54" aria-hidden="true">
    <circle cx="27" cy="27" r="25" fill="none" stroke="#e5e7e9" stroke-width="2.5"/>
    <circle cx="27" cy="27" r="25" fill="none" stroke="#e8411e" stroke-width="2.5" stroke-dasharray="19 158" transform="rotate(-90 27 27)" stroke-linecap="round"/>
  </svg>
  <div class="abs score-ring__value">275</div>
  <div class="abs score-ring__total">275/805</div>
  <div class="abs meta">
    <span class="meta__item"><svg width="9" height="9" viewBox="0 0 10 10" fill="none" stroke="#8f979e" stroke-width=".8"><rect x="1" y="1.8" width="8" height="7.4" rx="1"/><path d="M1 4h8M3 .8v2M7 .8v2"/></svg>September 4, 2024</span>
    <span class="meta__item"><svg width="8" height="9" viewBox="0 0 8 10" fill="none" stroke="#8f979e" stroke-width=".8"><path d="M1 .6h4l2 2v6.8H1z M2.5 5h3M2.5 7h3"/></svg>Simulation test 2</span>
  </div>
  <p class="abs summary">From classic novels like "Morning at Wrenfield" by Clara Whitcombe to contemporary bestsellers like "The Lantern Keeper" by M.R. Ashdown, literature transcends time and culture, touching the hearts and minds of readers. The power of storytelling allows us to escape reality, gain empathy, and explore diverse perspectives, making literature an indispensable part of the human experience.</p>
  <nav class="abs tabs">
    <span class="tab" style="left:0">Quantitative reasoning</span>
    <span class="tab tab--active" style="left:118px">Overall performance</span>
    <span class="tab" style="left:225px">Verbal reasoning</span>
    <span class="tab" style="left:317px">Data insights</span>
  </nav>
  <h2 class="abs qa-heading">Question performance &amp; time management</h2>
  <div class="abs filters">
    <span class="filter filter--active">All answers</span>
    <span class="filter">Correct answers</span>
    <span class="filter">Incorrect answers</span>
  </div>
  <div class="abs avg-time">
    <svg width="21" height="22" viewBox="0 0 22 22" fill="none" stroke="#8f979e" stroke-width="1.2"><circle cx="11" cy="12.5" r="8.5"/><path d="M9 2h4M11 12.5l3.5-3.5"/></svg>
    <span>Average time taken<br>per question</span>
  </div>
  <div class="abs time-pill time-pill--expected"><strong>2 mins</strong><small>Expected</small></div>
  <div class="abs time-pill time-pill--you"><strong>1 mins</strong><small>You</small></div>
  <div class="abs question-table">
    <div class="question-table__head"><span style="left:16px">Question</span><span style="left:166px">Response time(minutes)</span><span style="left:317px">Performance</span><span style="left:467px">Question type</span></div>
    <div class="q-row" style="top:36px"><span class="q-num">1</span><span class="tag tag--bad" style="left:166px">0.01</span><span class="tag tag--bad" style="left:317px">Incorrect</span><span class="tag tag--type" style="left:467px">Quantitative reasoning</span></div>
    <div class="q-row" style="top:71px"><span class="q-num">1</span><span class="tag tag--good" style="left:166px">0.1</span><span class="tag tag--good" style="left:317px">Correct</span><span class="tag tag--type" style="left:467px">Quantitative reasoning</span></div>
    <div class="q-row" style="top:107px"><span class="q-num">1</span><span class="tag tag--bad" style="left:166px">0.01</span><span class="tag tag--bad" style="left:317px">Incorrect</span><span class="tag tag--type" style="left:467px">Quantitative reasoning</span></div>
  </div>
</section>

</body>
</html>
```